Silverpine Orbit Works Flyer

We need a one page promotional piece that explains what our company does, and the benefits it provides in a simple, elegant, easy to understand way. I would like to print it on glossy heavyweight paper to give a feel of high quality and legitimacy. I will include the logo, the tag line, and the main benefits that the company offers.

Tag line concept, may not need these exact words. "Lend us 5 minutes each morning, and we will guide you toward a Silverpine Orbit Works."

Key points...(exact wording not required if you think of a better way to say it)

Software easy enough for my grandpa to use.
Lets you use snail mail, email, texting, and social media to quickly market to your customers at very low cost.
Web based which allows you to launch media campaigns from your desktop, or smartphone in moments.
Quick 3 - 5 minute training videos which give you hard hitting, quick action tips that will help you make your business better today.
Live coaching calls to help motivate you to improve your business.
No contracts, or start up fees. One low price of $299 per month.

Restaurant owners

Restaurant

```html
<!DOCTYPE html>
<html lang="en">
<head>
<meta charset="utf-8">
<title>Silverpine Orbit Works Flyer</title>
<link rel="stylesheet" href="https://fonts.googleapis.com/css2?family=PT+Sans+Narrow:wght@400;700&family=Roboto+Slab:wght@700&display=swap">
<style>
  :root {
    --paper: #ffffff;
    --ink: #3b3b3b;
    --brand-grey: #6e6e6e;
    --brand-green: #5a9a2a;
    --accent: #f7c31b;
    --panel-dark: #222222;
    --panel-mid: #4d4d4d;
    --panel-light: #8d8d8d;
    --rule: #4a4a4a;
    --bar: #2c2c2c;
    --white: #ffffff;
  }
  * { margin: 0; padding: 0; box-sizing: border-box; }
  html, body { width: 849px; height: 1200px; overflow: hidden; background: var(--paper); }
  .flyer {
    position: relative;
    width: 849px;
    height: 1200px;
    overflow: hidden;
    background: var(--paper);
    font-family: "PT Sans Narrow", "Arial Narrow", sans-serif;
    color: var(--ink);
  }
  .backdrop {
    position: absolute; inset: 0;
    background:
      radial-gradient(ellipse 160px 70px at 130px 70px, rgba(150,150,150,.22), transparent 70%),
      radial-gradient(ellipse 150px 70px at 760px 190px, rgba(150,150,150,.2), transparent 70%),
      radial-gradient(ellipse 120px 140px at 40px 330px, rgba(150,150,150,.2), transparent 70%),
      radial-gradient(ellipse 130px 90px at 820px 520px, rgba(150,150,150,.16), transparent 70%),
      radial-gradient(ellipse 140px 90px at 30px 800px, rgba(150,150,150,.16), transparent 70%),
      radial-gradient(ellipse 150px 90px at 300px 1160px, rgba(150,150,150,.18), transparent 70%),
      radial-gradient(ellipse 160px 90px at 780px 1150px, rgba(150,150,150,.18), transparent 70%);
  }
  .brand {
    position: absolute; left: 0; right: 0; top: 150px;
    display: flex; flex-direction: column; align-items: center; gap: 26px;
  }
  .brand-mark {
    width: 120px; height: 120px; border-radius: 50%;
    background: var(--brand-grey);
  }
  .brand-name {
    font-family: "PT Sans Narrow", "Arial Narrow", sans-serif;
    font-weight: 700;
    font-size: 44px;
    color: var(--brand-grey);
    letter-spacing: 1px;
  }
  .tagline {
    position: absolute; left: 0; right: 0; top: 396px;
    text-align: center;
    font-size: 27px; line-height: 35px;
    color: var(--ink);
  }
  .tagline strong { font-weight: 700; }
  .tagline .highlight { color: var(--brand-green); }
  .divider {
    position: absolute; left: 120px; top: 494px;
    width: 612px; height: 2px; background: var(--rule);
  }
  .benefits { position: absolute; left: 80px; top: 504px; width: 696px; }
  .benefit {
    position: absolute; left: 0; width: 696px;
    display: flex; align-items: center; justify-content: center;
    text-align: center;
    color: var(--white);
    font-size: 26px; line-height: 32px;
    background: linear-gradient(165deg, var(--panel-dark) 0%, var(--panel-mid) 55%, var(--panel-light) 100%);
    border-bottom: 4px solid #f2f2f2;
    box-shadow: 0 2px 3px rgba(0,0,0,.25);
  }
  .benefit strong { font-weight: 700; }
  .benefit .accent { color: var(--accent); }
  .benefit-ease     { top: 0;   height: 60px; }
  .benefit-channels { top: 66px; height: 92px; }
  .benefit-web      { top: 164px; height: 98px; }
  .benefit-training { top: 268px; height: 138px; }
  .benefit-coaching { top: 412px; height: 102px; }
  .price-bar {
    position: absolute; left: 57px; top: 1030px;
    width: 734px; height: 50px;
    background: var(--bar);
    display: flex; align-items: center; justify-content: center;
    font-size: 26px; color: var(--accent);
  }
  .price-bar strong { font-weight: 700; }
</style>
</head>
<body>
<main class="flyer">
  <div class="backdrop" role="img" aria-label="Faint scattered banknotes floating across the page"></div>

  <header class="brand">
    <div class="brand-mark"></div>
    <div class="brand-name">Silverpine Orbit Works</div>
  </header>

  <p class="tagline">Lend us 5 minutes each morning, and we will guide you<br>toward a <strong>Silverpine <span class="highlight">Orbit</span> Works</strong>.</p>

  <div class="divider"></div>

  <section class="benefits">
    <div class="benefit benefit-ease"><p>Software <span class="accent">easy</span> enough <strong>for my grandpa to use.</strong></p></div>
    <div class="benefit benefit-channels"><p>Lets you use snail mail, email, texting, and social media<br><strong>to quickly market to your customers at <span class="accent">very low cost</span>.</strong></p></div>
    <div class="benefit benefit-web"><p>Web based so you can launch media campaigns<br><strong><span class="accent">from your desktop or smartphone</span> in moments.</strong></p></div>
    <div class="benefit benefit-training"><p>Quick 3 - 5 minute training videos which give you <strong>hard<br>hitting, quick action tips that will help you<br><span class="accent">make your business better today</span>.</strong></p></div>
    <div class="benefit benefit-coaching"><p>Live coaching calls to <strong>help motivate you<br>to <span class="accent">improve your business</span>.</strong></p></div>
  </section>

  <div class="price-bar"><p>No contracts or start up fees. <strong>One low price of $299 per month.</strong></p></div>
</main>
</body>
</html>
```